3 Page Design for Bluefern Capital

We want a Home Page, About Page, and Products & Services Page for Bluefern Capital. Please refer to the attached docs for more info.
If done in Figma, would like Figma files that can easily be ported to Wordpress.

```html
<!DOCTYPE html>
<html lang="en">
<head>
<meta charset="utf-8">
<title>Bluefern Capital – Page Designs</title>
<link href="https://fonts.googleapis.com/css2?family=Roboto:ital,wght@0,400;0,500;0,700;1,400&display=swap" rel="stylesheet">
<style>
:root{
  --board:#c2b5a2;
  --sand:#e6dac6;
  --sand-light:#ede3d4;
  --brown:#8b6a3e;
  --red:#9b1c2e;
  --tan:#8b7355;
  --ink:#2d2d2d;
  --muted:#9a9a9a;
  --dark:#333333;
  --darker:#2e2e2e;
  --line:#6e6c86;
  --white:#ffffff;
}
*{box-sizing:border-box;margin:0;padding:0}
html,body{width:1200px;height:1200px;overflow:hidden;background:var(--board)}
body{font-family:"Roboto",Arial,sans-serif;color:var(--ink)}
.board{position:absolute;left:0;top:0;width:1932px;height:1932px;transform:scale(0.62112);transform-origin:0 0;background:var(--board)}
.page-label{position:absolute;top:90px;width:300px;margin-left:-150px;text-align:center;font-size:26px;color:#4a4a4a;font-weight:400}
.page{position:absolute;background:var(--white);overflow:hidden}
.a{position:absolute}
.center{text-align:center}
.band-sand{background:var(--sand)}
.h-sec{font-size:14px;font-weight:500;color:var(--brown);text-align:center;left:0;right:0}
.sub{font-size:5.5px;color:var(--muted);text-align:center;left:0;right:0;line-height:9px}
.body-s{font-size:5.6px;color:var(--muted);line-height:10px}
.btn{display:flex;align-items:center;justify-content:center;gap:3px;font-size:5.5px;font-weight:500;color:#fff;border-radius:2px}
.btn-red{background:var(--red)}
.btn-tan{background:var(--tan)}
.card{background:#fff;border-radius:3px;box-shadow:0 1px 4px rgba(0,0,0,.08)}
.icon{border-radius:50%;background:var(--sand);display:flex;align-items:center;justify-content:center}
.icon i{display:block;width:7px;height:7px;background:var(--brown);border-radius:1px}
.photo{border-radius:3px;box-shadow:0 3px 10px rgba(0,0,0,.2)}
.photo-office{background:linear-gradient(135deg,#f1eeea 0%,#d9d4cc 45%,#b7aea3 75%,#6f6861 100%)}
.photo-desk{background:linear-gradient(135deg,#ececea 0%,#d2d0cc 50%,#8e8b86 80%,#3c3a38 100%)}
.card-title{font-size:10px;font-weight:500;color:var(--ink);text-align:center;left:0;right:0}
.card-text{font-size:5.5px;color:var(--muted);line-height:10px;text-align:center;left:12px;right:12px}
/* nav */
.nav-logo-dot{width:18px;height:18px;border-radius:50%;background:var(--ink)}
.nav-name{font-size:10px;font-weight:700;color:var(--ink)}
.nav-link{font-size:5.5px;color:var(--ink)}
/* stats */
.stat{border-top:2px solid var(--line)}
.stat-num{font-size:14px;font-weight:500;color:var(--brown);text-align:center;left:0;right:0}
.stat-label{font-size:5.5px;color:var(--muted);text-align:center;left:0;right:0}
/* dark */
.dark{background:var(--dark)}
.dark-title{font-size:14px;font-weight:500;color:var(--sand);text-align:center;left:0;right:0}
.dark-sub{font-size:5.6px;color:#aaa;text-align:center;line-height:10px}
.footer{background:var(--darker)}
.foot-h{font-size:7px;font-weight:700;color:#e8e0d2}
.foot-t{font-size:5.6px;color:#a9a9a9;line-height:10.5px}
.foot-links div{font-size:5.3px;color:#a9a9a9;line-height:13.6px}
.social{width:13px;height:13px;border-radius:50%;background:#4a4a4a}
.foot-rule{height:1px;background:#444}
.copy{font-size:5.5px;color:#a9a9a9;text-align:center;left:0;right:0}
/* services */
.svc{border-left:2px solid var(--line)}
.svc-title{font-size:9.5px;font-weight:500;color:var(--ink);line-height:12px}
.checks div{font-size:4.8px;color:var(--muted);line-height:14px}
.checks b{color:var(--tan);font-weight:700;margin-right:4px}
.field-label{font-size:5px;color:var(--ink)}
.field{background:#fff;border:1px solid #c9c2b6;border-radius:2px;font-size:5px;color:var(--ink);padding-left:5px;display:flex;align-items:center}
.form-field{border:1px solid #bbb;border-radius:2px;font-size:5px;color:#777;padding-left:6px;display:flex;align-items:center;background:#fff}
.step{width:26px;height:26px;border-radius:50%;background:var(--sand);font-size:7px;color:var(--brown);display:flex;align-items:center;justify-content:center}
.avatar{width:44px;height:44px;border-radius:50%;background:linear-gradient(160deg,#d8d4cf,#7d746b)}
</style>
</head>
<body>
<div class="board">

  <div class="page-label" style="left:340px">Home</div>
  <div class="page-label" style="left:949px">About</div>
  <div class="page-label" style="left:1596px">Services</div>

  <!-- HOME -->
  <section class="page" style="left:90px;top:151px;width:515px;height:1216px">
    <header class="a" style="left:0;top:0;width:515px;height:34px;background:#fff">
      <div class="a nav-logo-dot" style="left:24px;top:8px"></div>
      <div class="a nav-name" style="left:48px;top:11px">Bluefern Capital</div>
      <div class="a nav-link" style="left:338px;top:14px;color:var(--brown);text-decoration:underline">Home</div>
      <div class="a nav-link" style="left:366px;top:14px">About</div>
      <div class="a nav-link" style="left:392px;top:14px">Services</div>
      <div class="a btn btn-red" style="left:427px;top:7px;width:51px;height:19px">Contact Us</div>
    </header>

    <div class="a band-sand" style="left:0;top:34px;width:515px;height:242px"></div>
    <h1 class="a" style="left:46px;top:92px;font-size:20px;line-height:24px;font-weight:700;color:var(--ink)">Where Discipline<br>Meets Wealth</h1>
    <p class="a body-s" style="left:46px;top:148px;width:200px;font-size:6.2px;line-height:11px">Refined financial strategy for athletes in transition. Building generational success on and off the field through the discipline of sports and structure of business.</p>
    <div class="a btn btn-red" style="left:46px;top:199px;width:66px;height:19px">➤ Our Services</div>
    <div class="a btn btn-tan" style="left:118px;top:199px;width:61px;height:19px">● Learn More</div>
    <div class="a photo photo-office" style="left:270px;top:63px;width:199px;height:184px" role="img" aria-label="Photo of a team meeting with sticky notes on a whiteboard"></div>
    <div class="a" style="left:278px;top:149px;width:12px;height:12px;border-radius:50%;background:rgba(255,255,255,.8)"></div>
    <div class="a" style="left:448px;top:149px;width:12px;height:12px;border-radius:50%;background:rgba(255,255,255,.8)"></div>

    <div class="a card stat" style="left:46px;top:300px;width:95px;height:96px">
      <div class="a icon" style="left:38px;top:16px;width:20px;height:20px"><i></i></div>
      <div class="a stat-num" style="top:48px">250</div>
      <div class="a stat-label" style="top:74px">Successful Clients</div>
    </div>
    <div class="a card stat" style="left:156px;top:300px;width:95px;height:96px">
      <div class="a icon" style="left:38px;top:16px;width:20px;height:20px"><i></i></div>
      <div class="a stat-num" style="top:48px">850</div>
      <div class="a stat-label" style="top:74px">Assets Managed ($M)</div>
    </div>
    <div class="a card stat" style="left:265px;top:300px;width:95px;height:96px">
      <div class="a icon" style="left:38px;top:16px;width:20px;height:20px"><i></i></div>
      <div class="a stat-num" style="top:48px">15</div>
      <div class="a stat-label" style="top:74px">Years of Experience</div>
    </div>
    <div class="a card stat" style="left:374px;top:300px;width:95px;height:96px">
      <div class="a icon" style="left:38px;top:16px;width:20px;height:20px"><i></i></div>
      <div class="a stat-num" style="top:48px">98</div>
      <div class="a stat-label" style="top:74px">Client Satisfaction</div>
    </div>

    <h2 class="a h-sec" style="top:450px">Built for Legacy. Designed for Performance.</h2>
    <p class="a sub" style="top:474px;left:120px;right:120px">Our approach combines the discipline of sports with the structure of business to create lasting financial success.</p>

    <div class="a card" style="left:46px;top:519px;width:131px;height:137px">
      <div class="a icon" style="left:51px;top:15px;width:28px;height:28px"><i></i></div>
      <div class="a card-title" style="top:53px">Athlete-Focused</div>
      <p class="a card-text" style="top:72px">Specialized financial strategies designed specifically for professional athletes and their unique career timelines.</p>
    </div>
    <div class="a card" style="left:193px;top:519px;width:131px;height:137px">
      <div class="a icon" style="left:51px;top:15px;width:28px;height:28px"><i></i></div>
      <div class="a card-title" style="top:53px">Wealth Building</div>
      <p class="a card-text" style="top:72px">Comprehensive investment and wealth management strategies to secure your financial future beyond your playing career.</p>
    </div>
    <div class="a card" style="left:339px;top:519px;width:131px;height:137px">
      <div class="a icon" style="left:51px;top:15px;width:28px;height:28px"><i></i></div>
      <div class="a card-title" style="top:53px">Transition Planning</div>
      <p class="a card-text" style="top:72px">Strategic guidance for athletes navigating career transitions and building sustainable post-career success.</p>
    </div>

    <div class="a band-sand" style="left:0;top:687px;width:515px;height:224px"></div>
    <h2 class="a h-sec" style="top:721px">Success Stories</h2>
    <p class="a sub" style="top:745px">Hear from athletes who have successfully transitioned to financial prosperity</p>
    <div class="a" style="left:112px;top:788px;font-size:12px;color:#aaa">“</div>
    <p class="a" style="left:120px;right:120px;top:790px;font-size:7px;line-height:12px;font-style:italic;color:var(--ink);text-align:center">"As an entrepreneur and former athlete, I needed a financial partner who understood both worlds. Bluefern Capital delivered beyond my expectations."</p>
    <div class="a" style="left:398px;top:800px;font-size:12px;color:#aaa">”</div>
    <div class="a" style="left:180px;top:826px;width:22px;height:22px;border-radius:50%;background:linear-gradient(160deg,#cfc9c1,#6c645c)" role="img" aria-label="Client portrait"></div>
    <div class="a" style="left:256px;top:828px;font-size:5.5px;font-weight:700">Evan Brooks</div>
    <div class="a" style="left:208px;top:838px;font-size:5px;color:var(--muted)">Former Pro Basketball Player, Tech Entrepreneur</div>
    <div class="a" style="left:245px;top:871px;width:4px;height:4px;border-radius:50%;background:#aaa"></div>
    <div class="a" style="left:255px;top:871px;width:4px;height:4px;border-radius:50%;background:#aaa"></div>
    <div class="a" style="left:265px;top:871px;width:4px;height:4px;border-radius:50%;background:var(--brown)"></div>

    <div class="a dark" style="left:0;top:911px;width:515px;height:153px">
      <svg class="a" style="left:0;top:0" width="515" height="153"><polygon points="0,80 515,20 515,153 0,153" fill="#2f2f2f"/></svg>
      <h2 class="a dark-title" style="top:37px">Ready to Build Your Legacy?</h2>
      <p class="a dark-sub" style="top:62px;left:130px;right:130px">Schedule a consultation with our team to develop a personalized financial strategy for your unique needs and goals.</p>
      <div class="a btn btn-red" style="left:218px;top:98px;width:79px;height:19px">▣ Get Started Today</div>
    </div>

    <footer class="a footer" style="left:0;top:1064px;width:515px;height:152px">
      <div class="a foot-h" style="left:46px;top:24px">Bluefern Capital</div>
      <p class="a foot-t" style="left:46px;top:41px;width:125px">Where discipline meets wealth. Building generational success for athletes and entrepreneurs.</p>
      <div class="a social" style="left:46px;top:82px"></div><div class="a social" style="left:67px;top:82px"></div><div class="a social" style="left:88px;top:82px"></div><div class="a social" style="left:108px;top:82px"></div>
      <div class="a foot-h" style="left:193px;top:24px">Quick Links</div>
      <div class="a foot-links" style="left:193px;top:40px"><div>Home</div><div>About</div><div>Services</div><div>Contact</div></div>
      <div class="a foot-h" style="left:340px;top:24px">Contact Us</div>
      <div class="a foot-links" style="left:340px;top:40px"><div>✉ hello@blueferncapital.com</div><div>✆ (555) 010-2288</div><div>⌖ 48 Summit Row, Suite 210</div></div>
      <div class="a foot-rule" style="left:46px;right:46px;top:114px"></div>
      <div class="a copy" style="top:127px">© 2025 Bluefern Capital. All rights reserved. | Privacy Policy | Terms of Service</div>
    </footer>
  </section>

  <!-- ABOUT -->
  <section class="page" style="left:710px;top:151px;width:515px;height:1211px">
    <div class="a band-sand" style="left:0;top:0;width:515px;height:116px">
      <svg class="a" style="left:0;top:0" width="515" height="116"><path d="M0,0 H515 V40 Q260,5 0,70 Z" fill="#ece3d5"/></svg>
    </div>
    <h1 class="a" style="left:0;right:0;top:31px;text-align:center;font-size:20px;font-weight:700;color:var(--ink)">About Bluefern Capital</h1>
    <p class="a sub" style="top:62px">Bridging the worlds of performance, wealth, and wellness for athletes and entrepreneurs</p>

    <h2 class="a" style="left:45px;top:147px;font-size:14px;font-weight:500;color:var(--brown)">Our Mission</h2>
    <p class="a body-s" style="left:45px;top:171px;width:202px">Bluefern Capital was founded on the principle that the discipline required for athletic excellence can be channeled into building lasting financial success. We help athletes and entrepreneurs create generational wealth through refined strategies that balance performance with long-term stability.</p>
    <p class="a body-s" style="left:45px;top:232px;width:202px">Our approach merges the structure of business with the power of automation to create sustainable financial systems that work for you, not against you.</p>
    <div class="a btn btn-red" style="left:45px;top:274px;width:67px;height:19px">⚯ Our Services</div>
    <div class="a photo photo-office" style="left:268px;top:145px;width:200px;height:147px" role="img" aria-label="Photo of advisors planning with sticky notes in an office"></div>

    <div class="a band-sand" style="left:0;top:325px;width:515px;height:243px"></div>
    <h2 class="a h-sec" style="top:354px">Our Values</h2>
    <p class="a sub" style="top:378px">The principles that guide our approach to wealth management</p>
    <div class="a card" style="left:45px;top:411px;width:131px;height:127px">
      <div class="a icon" style="left:51px;top:16px;width:28px;height:28px"><i></i></div>
      <div class="a card-title" style="top:53px">Discipline</div>
      <p class="a card-text" style="top:72px">Applying the same focus and consistency from athletic training to financial planning.</p>
    </div>
    <div class="a card" style="left:191px;top:411px;width:131px;height:127px">
      <div class="a icon" style="left:51px;top:16px;width:28px;height:28px"><i></i></div>
      <div class="a card-title" style="top:53px">Trust</div>
      <p class="a card-text" style="top:72px">Building long-term relationships based on transparency and proven results.</p>
    </div>
    <div class="a card" style="left:337px;top:411px;width:131px;height:127px">
      <div class="a icon" style="left:51px;top:16px;width:28px;height:28px"><i></i></div>
      <div class="a card-title" style="top:53px">Innovation</div>
      <p class="a card-text" style="top:72px">Leveraging cutting-edge strategies and technology to optimize financial outcomes.</p>
    </div>

    <h2 class="a h-sec" style="top:598px">Our Process</h2>
    <p class="a sub" style="top:622px">A structured approach to building your financial legacy</p>
    <div class="a" style="left:91px;top:669px;width:331px;height:1px;background:#ddd"></div>
    <div class="a step" style="left:118px;top:656px">1</div>
    <div class="a step" style="left:198px;top:656px">2</div>
    <div class="a step" style="left:283px;top:656px">3</div>
    <div class="a step" style="left:368px;top:656px">4</div>
    <div class="a card-title" style="left:91px;right:auto;width:80px;top:693px">Discovery</div>
    <div class="a card-title" style="left:171px;right:auto;width:80px;top:693px">Strategy</div>
    <div class="a card-title" style="left:251px;right:auto;width:90px;top:693px">Implementation</div>
    <div class="a card-title" style="left:341px;right:auto;width:80px;top:693px">Monitoring</div>
    <p class="a card-text" style="left:96px;right:auto;width:70px;top:712px">We begin by understanding your unique financial situation, goals, and values.</p>
    <p class="a card-text" style="left:176px;right:auto;width:70px;top:712px">We develop a customized financial plan tailored to your specific needs.</p>
    <p class="a card-text" style="left:258px;right:auto;width:76px;top:712px">We put your plan into action with precision and attention to detail.</p>
    <p class="a card-text" style="left:344px;right:auto;width:74px;top:712px">We continuously track and adjust your plan to ensure optimal performance.</p>

    <h2 class="a h-sec" style="top:832px">Our Leadership Team</h2>
    <p class="a sub" style="top:856px">Experienced professionals dedicated to your financial success</p>
    <div class="a card" style="left:45px;top:890px;width:131px;height:140px">
      <div class="a avatar" style="left:43px;top:12px" role="img" aria-label="Team member portrait"></div>
      <div class="a card-title" style="top:68px">Marcus Hale</div>
      <div class="a center" style="left:0;right:0;top:84px;font-size:5px;color:var(--brown)">CEO &amp; Founder</div>
      <p class="a card-text" style="top:98px">Former professional athlete with 15+ years in wealth management.</p>
    </div>
    <div class="a card" style="left:191px;top:890px;width:131px;height:140px">
      <div class="a avatar" style="left:43px;top:12px" role="img" aria-label="Team member portrait"></div>
      <div class="a card-title" style="top:68px">Nora Whitfield</div>
      <div class="a center" style="left:0;right:0;top:84px;font-size:5px;color:var(--brown)">Chief Financial Officer</div>
      <p class="a card-text" style="top:98px">CFA with expertise in portfolio management and financial planning.</p>
    </div>
    <div class="a card" style="left:337px;top:890px;width:131px;height:140px">
      <div class="a avatar" style="left:43px;top:12px" role="img" aria-label="Team member portrait"></div>
      <div class="a card-title" style="top:68px">Evan Brooks</div>
      <div class="a center" style="left:0;right:0;top:84px;font-size:5px;color:var(--brown)">Head of Strategy</div>
      <p class="a card-text" style="top:98px">Specializes in career transition planning and business development.</p>
    </div>

    <footer class="a footer" style="left:0;top:1060px;width:515px;height:151px">
      <div class="a foot-h" style="left:45px;top:24px">Bluefern Capital</div>
      <p class="a foot-t" style="left:45px;top:41px;width:125px">Where discipline meets wealth. Building generational success for athletes and entrepreneurs.</p>
      <div class="a social" style="left:45px;top:82px"></div><div class="a social" style="left:66px;top:82px"></div><div class="a social" style="left:87px;top:82px"></div><div class="a social" style="left:107px;top:82px"></div>
      <div class="a foot-h" style="left:191px;top:24px">Quick Links</div>
      <div class="a foot-links" style="left:191px;top:40px"><div>Home</div><div>About</div><div>Services</div><div>Contact</div></div>
      <div class="a foot-h" style="left:338px;top:24px">Contact Us</div>
      <div class="a foot-links" style="left:338px;top:40px"><div>✉ hello@blueferncapital.com</div><div>✆ (555) 010-2288</div><div>⌖ 48 Summit Row, Suite 210</div></div>
      <div class="a foot-rule" style="left:45px;right:45px;top:113px"></div>
      <div class="a copy" style="top:126px">© 2025 Bluefern Capital. All rights reserved. | Privacy Policy | Terms of Service</div>
    </footer>
  </section>

  <!-- SERVICES -->
  <section class="page" style="left:1319px;top:151px;width:515px;height:1630px">
    <div class="a band-sand" style="left:0;top:0;width:515px;height:46px">
      <svg class="a" style="left:0;top:0" width="515" height="46"><path d="M250,0 H515 V22 Q390,0 250,0 Z" fill="#ece3d5"/></svg>
    </div>
    <div class="a photo photo-desk" style="left:50px;top:76px;width:199px;height:147px" role="img" aria-label="Photo of financial documents and a calculator on a desk"></div>
    <h1 class="a" style="left:273px;top:86px;font-size:14px;line-height:17px;font-weight:500;color:var(--brown)">Refined Strategy for<br>Athletes in Transition</h1>
    <p class="a body-s" style="left:273px;top:126px;width:200px">Our specialized services are designed to address the unique financial challenges and opportunities that professional athletes face throughout their careers and beyond.</p>
    <p class="a body-s" style="left:273px;top:167px;width:200px">We provide comprehensive wealth management solutions that align with your values, goals, and timeline.</p>
    <div class="a btn btn-red" style="left:273px;top:197px;width:92px;height:19px">▣ Schedule Consultation</div>

    <div class="a card svc" style="left:50px;top:244px;width:130px;height:197px">
      <div class="a icon" style="left:14px;top:16px;width:20px;height:20px"><i></i></div>
      <div class="a svc-title" style="left:14px;top:46px">Wealth<br>Management</div>
      <p class="a body-s" style="left:14px;top:76px;width:106px;font-size:5px">Comprehensive investment strategies tailored to your financial goals and risk tolerance.</p>
      <div class="a checks" style="left:14px;top:112px"><div><b>✓</b>Portfolio Management</div><div><b>✓</b>Retirement Planning</div><div><b>✓</b>Tax Optimization</div><div><b>✓</b>Risk Assessment</div></div>
    </div>
    <div class="a card svc" style="left:196px;top:244px;width:130px;height:197px">
      <div class="a icon" style="left:14px;top:16px;width:20px;height:20px"><i></i></div>
      <div class="a svc-title" style="left:14px;top:46px">Career Transition<br>Planning</div>
      <p class="a body-s" style="left:14px;top:76px;width:106px;font-size:5px">Strategic guidance for athletes navigating the transition from active competition to post-career life.</p>
      <div class="a checks" style="left:14px;top:122px"><div><b>✓</b>Income Diversification</div><div><b>✓</b>Business Ventures</div><div><b>✓</b>Brand Development</div><div><b>✓</b>Skill Translation</div></div>
    </div>
    <div class="a card svc" style="left:342px;top:244px;width:130px;height:197px">
      <div class="a icon" style="left:14px;top:16px;width:20px;height:20px"><i></i></div>
      <div class="a svc-title" style="left:14px;top:46px">Legacy &amp; Estate<br>Planning</div>
      <p class="a body-s" style="left:14px;top:76px;width:106px;font-size:5px">Creating lasting financial structures to protect and pass on wealth to future generations.</p>
      <div class="a checks" style="left:14px;top:112px"><div><b>✓</b>Estate Planning</div><div><b>✓</b>Trust Services</div><div><b>✓</b>Philanthropic Strategy</div><div><b>✓</b>Wealth Transfer</div></div>
    </div>
    <div class="a card svc" style="left:50px;top:457px;width:130px;height:184px">
      <div class="a icon" style="left:14px;top:16px;width:20px;height:20px"><i></i></div>
      <div class="a svc-title" style="left:14px;top:46px">Financial Education</div>
      <p class="a body-s" style="left:14px;top:64px;width:100px;font-size:5px">Empowering clients with the knowledge to make informed financial decisions throughout their lives.</p>
      <div class="a checks" style="left:14px;top:112px"><div><b>✓</b>Financial Literacy Programs</div><div><b>✓</b>Investment Education</div><div><b>✓</b>Wealth Preservation Strategies</div><div><b>✓</b>Budgeting &amp; Cash Flow</div></div>
    </div>

    <h2 class="a h-sec" style="top:701px">Financial Resources</h2>
    <p class="a sub" style="top:726px">Tools to help you plan your financial future</p>

    <div class="a band-sand" style="left:50px;top:759px;width:422px;height:299px;border-radius:3px">
      <div class="a center" style="left:0;right:0;top:14px;font-size:9px;font-weight:500">Retirement Savings Calculator</div>
      <div class="a field-label" style="left:14px;top:40px">Current Age</div>
      <div class="a field" style="left:14px;top:51px;width:192px;height:17px">30</div>
      <div class="a field-label" style="left:215px;top:40px">Retirement Age</div>
      <div class="a field" style="left:215px;top:51px;width:193px;height:17px">65</div>
      <div class="a field-label" style="left:14px;top:88px">Current Savings ($)</div>
      <div class="a field" style="left:14px;top:99px;width:192px;height:17px">50000</div>
      <div class="a field-label" style="left:215px;top:88px">Monthly Contribution ($)</div>
      <div class="a field" style="left:215px;top:99px;width:193px;height:17px">1000</div>
      <div class="a field-label" style="left:14px;top:136px">Expected Annual Return (%)</div>
      <div class="a field" style="left:14px;top:147px;width:192px;height:17px">7</div>
      <div class="a field-label" style="left:215px;top:136px">Expected Inflation (%)</div>
      <div class="a field" style="left:215px;top:147px;width:193px;height:17px">2.5</div>
      <div class="a" style="left:14px;top:184px;width:394px;height:100px;background:#fff;border-radius:2px">
        <div class="a center" style="left:0;right:0;top:12px;font-size:12px;font-weight:500;color:var(--brown)">$1,181,279</div>
        <div class="a center" style="left:0;right:0;top:33px;font-size:5px;color:var(--muted)">Estimated retirement savings</div>
        <div class="a btn btn-red" style="left:170px;top:74px;width:54px;height:17px">▣ Calculate</div>
      </div>
    </div>

    <div class="a dark" style="left:0;top:1088px;width:515px;height:542px">
      <svg class="a" style="left:0;top:0" width="515" height="542"><polygon points="0,70 515,250 515,542 0,542" fill="#2f2f2f"/></svg>
      <h2 class="a dark-title" style="top:36px">Ready to Build Your Financial Legacy?</h2>
      <p class="a dark-sub" style="top:61px;left:130px;right:130px">Contact us today to learn how our specialized services can help you achieve your financial goals.</p>
      <div class="a" style="left:114px;top:97px;width:294px;height:266px;background:#fff;border-radius:3px">
        <div class="a center" style="left:0;right:0;top:18px;font-size:10px;font-weight:500">Get In Touch</div>
        <div class="a center field-label" style="left:0;right:0;top:37px">Full Name</div>
        <div class="a form-field" style="left:18px;top:48px;width:258px;height:17px">Enter your name</div>
        <div class="a center field-label" style="left:0;right:0;top:76px">Email Address</div>
        <div class="a form-field" style="left:18px;top:87px;width:258px;height:17px">Enter your email</div>
        <div class="a center field-label" style="left:0;right:0;top:115px">Service Interest</div>
        <div class="a form-field" style="left:18px;top:126px;width:258px;height:17px;color:var(--ink);justify-content:space-between;padding-right:4px">Select a service<span>⌄</span></div>
        <div class="a center field-label" style="left:0;right:0;top:154px">Message</div>
        <div class="a form-field" style="left:18px;top:165px;width:258px;height:55px;align-items:flex-start;padding-top:5px">Tell us about your financial goals...</div>
        <div class="a btn btn-red" style="left:112px;top:232px;width:70px;height:16px">➤ Send Message</div>
      </div>
      <div class="a foot-h" style="left:50px;top:423px">Bluefern Capital</div>
      <p class="a foot-t" style="left:50px;top:440px;width:125px">Where discipline meets wealth. Building generational success for athletes and entrepreneurs.</p>
      <div class="a social" style="left:50px;top:481px"></div><div class="a social" style="left:71px;top:481px"></div><div class="a social" style="left:92px;top:481px"></div><div class="a social" style="left:112px;top:481px"></div>
      <div class="a foot-h" style="left:196px;top:423px">Quick Links</div>
      <div class="a foot-links" style="left:196px;top:439px"><div>Home</div><div>About</div><div>Services</div><div>Contact</div></div>
      <div class="a foot-h" style="left:343px;top:423px">Contact Us</div>
      <div class="a foot-links" style="left:343px;top:439px"><div>✉ hello@blueferncapital.com</div><div>✆ (555) 010-2288</div><div>⌖ 48 Summit Row, Suite 210</div></div>
      <div class="a foot-rule" style="left:50px;right:50px;top:514px"></div>
      <div class="a copy" style="top:527px">© 2025 Bluefern Capital. All rights reserved. | Privacy Policy | Terms of Service</div>
    </div>
  </section>

</div>
</body>
</html>
```